Kivo4 Website design (Need help to re-design our website)

We need someone to help us re-design our website and launch it. All contents for the website are ready. (Website: https://www.kivo4.com.au/)

-Rearrange categories:
1. Heat Pumps (Link to PALOX site: https://palox.com.au/)
2. Solar (Under the Solar category; remove solar panels, solar inverters, and solar batteries)
3. LED
4. Capability Statement
5. Service and Support
6. Contact us

Home page - redesign but the free quote will stay.

NOTE:
-Try using professional fonts (Example: Helvetica, etc.)
-Try to play with colours related to sustainability, eco-friendliness, solar, energy, and energy efficiency.
-The website's Footer should be readable and use light colour.

Target Market(s)

Residentials & commercial buildings

Industry/Entity Type

SOLAR ENERGY PROVIDER

Coding

Coded - Design and coding required

Colors

Designer to choose colors to be used in the design.

Requirements
Nice to have
• Effects/transition on the words/copy/images.

```html
<!DOCTYPE html>
<html lang="en">
<head>
<meta charset="utf-8">
<title>Kivo4 — Solar Energy Provider</title>
<link href="https://fonts.googleapis.com/css2?family=Montserrat:wght@600;700;800;900&family=Open+Sans:wght@400;600;700&display=swap" rel="stylesheet">
<style>
:root{
  --blue:#1366c9;
  --blue-dark:#0b3f86;
  --green:#2aa84a;
  --green-light:#5cc85a;
  --ink:#1f2733;
  --muted:#6b7380;
  --grey-band:#e9ebee;
  --line:#dde1e6;
  --night:#14181f;
  --white:#ffffff;
}
*{box-sizing:border-box;margin:0;padding:0}
html,body{width:1200px;height:3980px;overflow:hidden}
body{font-family:"Open Sans",Arial,sans-serif;color:var(--ink);background:var(--white);position:relative}
.h-title{font-family:"Montserrat",Arial,sans-serif;font-weight:900;letter-spacing:3px;text-transform:uppercase}
.grad{background:linear-gradient(90deg,var(--blue),var(--green));-webkit-background-clip:text;background-clip:text;color:transparent}
.btn{display:inline-flex;align-items:center;gap:8px;background:var(--blue);color:var(--white);font-weight:700;font-size:14px;padding:12px 24px;border-radius:3px}
section{position:absolute;left:0;width:1200px}

/* header */
.site-header{position:absolute;top:0;left:0;width:1200px;height:88px;background:var(--white);display:flex;align-items:center;padding:0 90px 0 120px;box-shadow:0 2px 6px rgba(0,0,0,.08);z-index:3}
.brand{display:flex;align-items:center;gap:10px;font-family:"Montserrat",sans-serif;font-weight:800;font-size:30px;color:var(--blue)}
.brand i{width:22px;height:22px;border-radius:50%;background:var(--green);display:block}
.nav{display:flex;gap:22px;margin-left:auto;font-size:13px;font-weight:600}
.call{margin-left:34px;display:flex;align-items:center;gap:8px;font-weight:700;font-size:13px}
.call span{width:26px;height:26px;border-radius:50%;background:var(--green);display:grid;place-items:center}

/* hero */
.hero{top:88px;height:500px;background:linear-gradient(160deg,#4a5563 0%,#262d36 55%,#1a2530 100%)}
.hero-copy{position:absolute;left:120px;top:110px;width:540px;color:var(--white)}
.hero-copy h1{font-size:44px;line-height:1.15;margin-bottom:24px}
.hero-copy h3{font-size:18px;margin-bottom:10px}
.hero-copy p{font-size:14px;line-height:1.6;margin-bottom:26px;opacity:.9}
.quote{position:absolute;left:700px;top:120px;width:390px;background:var(--white);box-shadow:0 10px 30px rgba(0,0,0,.25);z-index:2}
.quote h2{background:var(--blue);color:var(--white);font-family:"Montserrat",sans-serif;font-size:22px;text-align:center;padding:18px 0}
.quote form{padding:20px 28px 26px}
.field{border-bottom:1px solid var(--line);font-size:13px;color:var(--muted);padding:14px 0 8px;display:flex;justify-content:space-between}
.quote .btn{display:flex;justify-content:center;margin-top:22px}

/* partners */
.partners{top:700px;text-align:center}
.partners h2{font-size:36px}
.partners h2 .g{color:var(--green)}
.partners h2 .b{color:var(--blue)}
.badge-row{display:flex;justify-content:center;align-items:center;gap:26px;margin-top:34px}
.badge{width:152px;height:80px;border:1px solid var(--line);box-shadow:0 3px 8px rgba(0,0,0,.07);display:grid;place-items:center}
.badge b{width:90px;height:32px;border-radius:4px;display:block}
.arrow{width:34px;height:34px;border-radius:50%;display:grid;place-items:center}

/* about */
.about{top:920px;height:480px}
.about-art{position:absolute;left:240px;top:20px;width:320px;height:400px;background:linear-gradient(180deg,var(--green-light),var(--blue));border-radius:40% 40% 8px 8px;opacity:.85}
.about-copy{position:absolute;left:640px;top:180px;width:440px}
.about-copy h2{font-size:44px}
.about-copy p{font-size:13px;line-height:1.6;color:var(--muted);margin:14px 0}
.about-copy h4{font-family:"Montserrat",sans-serif;font-size:20px;color:var(--blue)}

/* projects */
.projects{top:1460px;height:620px;background:var(--grey-band)}
.projects h2{position:absolute;left:120px;top:30px;font-size:38px}
.tabs{position:absolute;right:80px;top:110px;display:flex;gap:10px}
.tab{font-size:13px;font-weight:700;padding:12px 18px;border:1px solid var(--ink);background:var(--white)}
.tab.on{background:var(--blue);color:var(--white);border-color:var(--blue)}
.cards{position:absolute;left:120px;top:190px;display:flex;gap:18px}
.card{width:236px;height:330px;position:relative}
.card .ph{width:100%;height:100%}
.card .cap{position:absolute;left:0;right:0;bottom:0;background:rgba(0,0,0,.55);color:var(--white);text-align:center;padding:12px 0;font-weight:700;font-size:15px}
.card .cap small{display:block;font-weight:400;font-size:11px}
.pager{position:absolute;right:120px;top:555px;display:flex;gap:10px}

/* reviews */
.reviews{top:2200px;text-align:center}
.reviews h2{font-size:40px;color:var(--blue)}
.review-row{display:flex;justify-content:center;align-items:center;gap:24px;margin-top:44px}
.review{width:310px;height:200px;background:var(--white);box-shadow:0 4px 14px rgba(0,0,0,.1);text-align:left;padding:24px;position:relative}
.review p{font-size:12.5px;line-height:1.55;color:var(--muted)}
.review .who{position:absolute;left:24px;bottom:20px;right:24px;display:flex;justify-content:space-between;font-size:13px;font-weight:700}
.stars{color:#f4b400;font-size:12px;letter-spacing:2px}

/* signup */
.signup{top:2760px;height:480px;background:linear-gradient(90deg,var(--night) 40%,#2a2f36 100%)}
.signup-copy{position:absolute;left:140px;top:70px;width:460px;color:var(--white)}
.signup-copy h2{font-size:44px;line-height:1.1}
.signup-copy h2 em{font-style:normal;color:var(--blue)}
.signup-copy p{font-size:12px;opacity:.8;margin:10px 0 24px}
.sub-form{display:flex;width:420px;border:1px solid #555}
.sub-form span{flex:1;padding:12px 14px;font-size:13px;color:#aaa}
.sub-form b{background:var(--blue);padding:12px 18px;font-size:13px}
.signup-art{position:absolute;left:640px;top:20px;width:520px;height:440px;background:radial-gradient(ellipse at 45% 55%,#5b6470 0%,#2a3038 55%,transparent 75%)}

/* clients */
.clients{top:3360px;height:120px;display:flex;align-items:center;padding-left:140px;gap:40px}
.clients .tag{background:var(--green);color:var(--white);font-family:"Montserrat",sans-serif;font-weight:700;font-size:20px;padding:22px 30px}
.client{font-family:"Montserrat",sans-serif;font-weight:800;font-size:22px;color:var(--ink);width:150px;text-align:center}

/* footer */
.footer{top:3580px;height:400px;background:linear-gradient(180deg,#1a78d6,var(--blue-dark));color:var(--white)}
.fcol{position:absolute;top:60px}
.fcol h5{font-family:"Montserrat",sans-serif;font-size:17px;margin-bottom:18px;letter-spacing:1px}
.fcol li{list-style:none;font-size:13px;margin-bottom:14px}
.fcol li b{display:block;font-size:14px}
.fbrand{position:absolute;left:870px;top:60px}
.fbrand .brand{color:var(--white)}
.fbrand .brand i{background:var(--green-light)}
.social{display:flex;gap:10px;margin-top:22px}
.social span{width:32px;height:32px;border-radius:50%;background:var(--green)}
.fbar{position:absolute;left:120px;right:120px;bottom:0;border-top:1px solid rgba(255,255,255,.3);padding:18px 0;font-size:12px;display:flex;justify-content:space-between}
</style>
</head>
<body>

<header class="site-header">
  <div class="brand"><i></i>Kivo4</div>
  <nav class="nav"><span>Heat Pumps</span><span>Solar ▾</span><span>Capability Statement</span><span>LED</span><span>Service &amp; Support</span><span>Contact Us</span></nav>
  <div class="call"><span><svg width="12" height="12" viewBox="0 0 24 24"><path fill="#fff" d="M6.6 10.8a15 15 0 0 0 6.6 6.6l2.2-2.2a1 1 0 0 1 1-.25 11 11 0 0 0 3.6.6 1 1 0 0 1 1 1V20a1 1 0 0 1-1 1A17 17 0 0 1 3 4a1 1 0 0 1 1-1h3.5a1 1 0 0 1 1 1 11 11 0 0 0 .6 3.6 1 1 0 0 1-.25 1z"/></svg></span>Call Us (1300) 482 615</div>
</header>

<section class="hero" role="img" aria-label="Rows of solar panels at dusk">
  <div class="hero-copy">
    <h1 class="h-title">Why pay excess for your electricity?</h1>
    <h3>Save On Electricity Costs By Switching To Solar!</h3>
    <p>Did you know that you could install a solar system for a lower price than your current electricity costs? If you are looking for electricity, why not go for greener, cleaner energy? It's that simple.</p>
    <span class="btn">Contact Us</span>
  </div>
</section>

<div class="quote">
  <h2>Want A Free Quote?</h2>
  <form>
    <div class="field">Your Name*</div>
    <div class="field">Phone*</div>
    <div class="field">Email*</div>
    <div class="field">I Am Interested In* <span>▾</span></div>
    <div class="field">How Did You Find Us* <span>▾</span></div>
    <div class="field">Please Enter A Valid Address*</div>
    <span class="btn">Submit Now</span>
  </form>
</div>

<section class="partners">
  <h2 class="h-title"><span class="b">Accreditations</span> <span class="g">&amp;</span> <span class="g">Partners</span></h2>
  <div class="badge-row">
    <div class="arrow" style="background:var(--line)"><svg width="10" height="10" viewBox="0 0 10 10"><path d="M7 1 3 5l4 4" stroke="#555" stroke-width="1.6" fill="none"/></svg></div>
    <div class="badge"><b style="background:#d33c2e"></b></div>
    <div class="badge"><b style="background:var(--green)"></b></div>
    <div class="badge"><b style="background:#c9362b"></b></div>
    <div class="badge"><b style="background:var(--green-light)"></b></div>
    <div class="badge"><b style="background:#3a9a45"></b></div>
    <div class="arrow" style="background:var(--green)"><svg width="10" height="10" viewBox="0 0 10 10"><path d="M3 1l4 4-4 4" stroke="#fff" stroke-width="1.6" fill="none"/></svg></div>
  </div>
</section>

<section class="about">
  <div class="about-art" role="img" aria-label="Illustration of a city skyline rising from spread wings"></div>
  <div class="about-copy">
    <h2 class="h-title"><span style="color:var(--blue)">About</span> <span style="color:var(--green)">Kivo4</span></h2>
    <p>Power bills have risen dramatically in Australia over the past decade, making energy bills amongst the highest utility expense for businesses and households alike.</p>
    <h4>That's where we come in!</h4>
    <p>We are a completely Australian Owned and Operated company that specialises in adapting the latest technologies to improve your energy efficiency and reduce costs.</p>
    <span class="btn">Read More</span>
  </div>
</section>

<section class="projects">
  <h2 class="h-title grad">Our Projects</h2>
  <div class="tabs"><span class="tab on">Residential Solar</span><span class="tab">Commercial Solar</span></div>
  <div class="cards">
    <div class="card"><div class="ph" role="img" aria-label="Aerial view of a solar farm" style="background:linear-gradient(180deg,#9fb7cf,#8a6f55)"></div><div class="cap">Ridge 3<small>600 KW</small></div></div>
    <div class="card"><div class="ph" role="img" aria-label="Solar panels on a warehouse roof" style="background:linear-gradient(180deg,#7fa6d0,#4d5c6e)"></div><div class="cap">Harbour Depot<small>400 KW</small></div></div>
    <div class="card"><div class="ph" role="img" aria-label="Rooftop solar array under blue sky" style="background:linear-gradient(180deg,#6aa2e0,#2e4c74)"></div><div class="cap">Corval Works<small>150 KW</small></div></div>
    <div class="card"><div class="ph" role="img" aria-label="Solar panels on a farm building" style="background:linear-gradient(180deg,#8fc0e8,#6a7b5a)"></div><div class="cap">Wren Orchards<small>100 KW</small></div></div>
  </div>
  <div class="pager">
    <div class="arrow" style="background:var(--white)"><svg width="10" height="10" viewBox="0 0 10 10"><path d="M7 1 3 5l4 4" stroke="#555" stroke-width="1.6" fill="none"/></svg></div>
    <div class="arrow" style="background:var(--blue)"><svg width="10" height="10" viewBox="0 0 10 10"><path d="M3 1l4 4-4 4" stroke="#fff" stroke-width="1.6" fill="none"/></svg></div>
  </div>
</section>

<section class="reviews">
  <h2 class="h-title">Customer Reviews</h2>
  <div class="review-row">
    <div class="arrow" style="background:var(--line)"><svg width="10" height="10" viewBox="0 0 10 10"><path d="M7 1 3 5l4 4" stroke="#555" stroke-width="1.6" fill="none"/></svg></div>
    <div class="review"><p>"Kivo4 are an awesome company with high levels of professionalism. Our panels were installed promptly with no issues. The team goes above and beyond to ensure their customers are happy. 100% recommended!"</p><div class="who">Tessa Marlowe <span class="stars">★★★★★</span></div></div>
    <div class="review"><p>"Very happy with the service Kivo4 delivered, on time as promised, no hidden cost and very professional. Always replied to all of my questions. Thank you for the great service, I totally recommend to use Kivo4 for your solar."</p><div class="who">Reina Okafor <span class="stars">★★★★★</span></div></div>
    <div class="review"><p>Very happy dealing with this company, very professional, creates confidence and builds great relationships with customers and have state of the art high-end products and customer service. Would highly recommend their services.</p><div class="who">Dana Vellacott <span class="stars">★★★★★</span></div></div>
    <div class="arrow" style="background:var(--green)"><svg width="10" height="10" viewBox="0 0 10 10"><path d="M3 1l4 4-4 4" stroke="#fff" stroke-width="1.6" fill="none"/></svg></div>
  </div>
</section>

<section class="signup">
  <div class="signup-copy">
    <h2 class="h-title"><em>Signup</em> for the latest offers</h2>
    <p>Get all the latest information on special discounts, products &amp; offers</p>
    <div class="sub-form"><span>Enter Your Email Here</span><b>Subscribe</b></div>
    <p style="margin-top:40px">You can download our capability statement by clicking below</p>
    <span class="btn">Download <svg width="12" height="12" viewBox="0 0 12 12"><path d="M6 1v7M3 5l3 3 3-3M2 11h8" stroke="#fff" stroke-width="1.6" fill="none"/></svg></span>
  </div>
  <div class="signup-art" role="img" aria-label="City skyline silhouette lit at night"></div>
</section>

<section class="clients">
  <span class="tag">Our Clients</span>
  <span class="client" style="color:#d43b2a">Tennarro</span>
  <span class="client" style="color:#1a1a1a">Lumtown</span>
  <span class="client" style="color:#c8202a">Ferrows</span>
  <span class="client" style="color:#d0101a">Parcelo</span>
</section>

<section class="footer">
  <div class="fcol" style="left:120px"><h5>QUICK LINKS</h5><ul><li>Heat Pumps</li><li>Solar</li><li>Capability Statement</li><li>LED</li><li>Service and Support</li><li>Contact Us</li></ul></div>
  <div class="fcol" style="left:330px"><h5>CONTACT DETAILS</h5><ul><li><b>Business Hours</b>Mon – Fri 9am – 5pm</li><li><b>Phone</b>(1300) 482 615</li><li><b>Email</b>info@kivo4.com.au</li></ul></div>
  <div class="fcol" style="left:590px"><h5>OFFICE LOCATIONS</h5><ul><li>52 Fenwick Road Altona VIC 3018</li><li>9/120 Casuarina Drive Nerang QLD 4211</li><li>31 Saltbush Way Bendigo VIC 3550</li><li>5/66 Coral Parade Joondalup WA 6027</li><li>18 Derwent Row Sandy Bay TAS 7005</li></ul></div>
  <div class="fbrand"><div class="brand"><i></i>Kivo4</div><div class="social"><span></span><span></span><span></span></div></div>
  <div class="fbar"><span>©2024 Kivo4. All Rights Reserved</span><span>Privacy Policy &nbsp;|&nbsp; Terms &nbsp;|&nbsp; FAQs</span></div>
</section>

</body>
</html>
```